Exciting Poster Project: 4 posters for Employee Benefit Program

We are an entrepreneurial healthcare IT company that is creating an internal campaign to launch our 2017 Culture and Professional Development goals for our internal staff.

We need 4 posters utilizing the 4 campaign logos (attached) that are tied together visually into a cohesive campaign.

A PPT is included that shows the other wall art that currently exists on the walls. The new posters will share a space with these pieces.

The posters may be mounted side by side, or stand alone on a wall- so the design should work both ways. Each poster should include its own icon and the tag line provided along with topics provided that fall under this category. The posters size can be dictated by your design, but the text should be legible from a minimum of 8 feet away.

At the bottom of each poster should include all 4 icons in order to tie the entire campaign together (perhaps they can be arranged together like a diamond shape with the primary one as the biggest diamond)

Our company website for our external branding is: www.pelmaroq.com
We have included our branding guidelines for our external brand, and ppts and graphics for our internal brand.

1) Poster 1:
a. Header: Better Today Than Yesterday
b. Sub-title: Personal and Professional Growth
c. Description: We are committed to helping you build on your strengths and passions and support you your career advancement goals. We have a variety of training and development programs available to help you reach your top potential!
Leadership Development Programs
1. Supervisor Training
2. Women’s Leadership
3. Leadership Meet-Ups
4. MBA Program
Staff Development
1. Continuing Education Fund
2. Book Club
3. Pelmaroq University
4. Mentorship
5. Learning Libraries
6. Department Wide Training Events

2) Poster 2:
a. Header: Perform at Highest Capacity
b. Sub-title: Be Your Best Self
c. Description: We are committed to providing programs that bring focus to your health and overall personal wellness to encourage a well balanced life
i. Healthy Living
1. Health and wellness seminars
2. Nutrition: Fruit Delivery
ii. Fitness:
1. Step Challenge
2. Virtual 5k
3. Recess
4. Golf Lessons
5. Ping Pong Club
iii. Creativity:
1. Painting
2. Photography Club
3. Virtual Trivia
iv. Mental Health:
1. Massage Therapy
2. EAP Education
v. Financial
1. 401(k)
2. Retirement education/financial planning seminars
3. Global Insurance Program education

3) Poster 3:
a. Header: Passionate Urgent and Driven to Success
b. Sub-Header: Innovation and Strategy
c. Description: We are committed to helping you connect the dots both in the industry and with our internal goals , mission, and vision.
i. Quarterly All-Hands
ii. Lumiverse
1. Internally: Departmental and Product Updates
2. Externally: Industry Knowledge
3. Culturally: Peer to Peer Community

4) Poster 4:
a. Header: Succeed as a Team
b. Sub-Header: Cultivating Collaboration
c. Description: We are committed to creating a culture of appreciation, teamwork, and supporting an open communication. All feedback and ideas are welcome here!
i. Team Building Events
1. Employee Focused
a. Summer Picnic
b. Employee Appreciation
c. Diwali
d. Holiday Party
e. Department Appreciation
2. Family Friendly
a. Halloween
b. Bring your Kids to Work Day
3. Awards
a. Peer to Peer: QuickNod Awards
b. Leadership: Crest of Merit
4. Surveys
a. New Hire
b. Employee Engagement
Updates

Target Market(s)

Internal Employees

Industry/Entity Type

Healthcare

Font styles to use
Sans Serif

Requirements
Must have
• Job Type: Posters
• Task Outline: Create Vector Art for 4 icons and 4 posters
• Fonts and Styles to Use: SourceSansPro
Nice to have
• There is an attachment with suggested concepts and styles that we like.
Should not have
• The poster should not be very wordy or hard to read in passing.

```html
<!DOCTYPE html>
<html lang="en">
<head>
<meta charset="utf-8">
<title>Pelmaroq Culture Campaign Posters</title>
<link href="https://fonts.googleapis.com/css2?family=Source+Sans+3:wght@400;600;700;900&display=swap" rel="stylesheet">
<style>
:root{
  --stage:#333333;
  --navy:#0f2a5c;
  --navy-deep:#0a1f47;
  --orange:#e9472c;
  --orange-light:#f26a48;
  --orange-brand:#ef5a24;
  --amber:#f3a234;
  --yellow:#f7c53a;
  --blue:#2f80cf;
  --blue-light:#3d8ddb;
  --green:#8cc63f;
  --purple:#6a2a8e;
  --purple-light:#7a3599;
  --white:#ffffff;
  --ink:#1d2f5a;
}
*{margin:0;padding:0;box-sizing:border-box}
html,body{width:1200px;height:480px;overflow:hidden;background:var(--stage)}
body{font-family:"Source Sans 3",sans-serif;color:var(--white);position:relative}
.poster{position:absolute;top:50px;width:265px;height:381px;overflow:hidden}
.poster--growth{left:42px;background:radial-gradient(circle at 55% 55%,#1a3a78,var(--navy-deep) 75%)}
.poster--wellness{left:322px;background:radial-gradient(circle at 50% 55%,var(--orange-light),var(--orange) 75%)}
.poster--innovation{left:605px;background:radial-gradient(circle at 50% 55%,var(--blue-light),var(--blue) 75%)}
.poster--team{left:887px;background:radial-gradient(circle at 50% 55%,var(--purple-light),var(--purple) 75%)}
.abs{position:absolute}
.headline{font-weight:900;text-transform:uppercase;line-height:.98;letter-spacing:.2px}
.tagline{font-weight:400}
.copy{font-size:7.4px;line-height:1.35}
.pill{display:inline-block;background:var(--white);border-radius:6px;padding:0 6px;font-size:7px;font-weight:700;line-height:9.5px;text-transform:uppercase;letter-spacing:.2px}
.list{list-style:none;margin-top:2px}
.list li{font-size:7px;line-height:10px;display:flex;align-items:center;white-space:nowrap}
.num{display:inline-flex;width:7.5px;height:7.5px;border-radius:50%;background:var(--white);font-size:5.5px;font-weight:700;align-items:center;justify-content:center;margin-right:4px;flex:none}
.diamond{position:absolute;border-radius:16%;transform:rotate(45deg)}
.base{position:absolute;left:0;top:344px;width:265px;height:37px}
.brand{position:absolute;top:356px;left:0;width:265px;display:flex;justify-content:center;align-items:center;gap:5px}
.brand__mark{width:12px;height:12px;background:var(--orange-brand);border-radius:2px}
.brand__name{font-size:14px;font-weight:700;color:var(--ink);letter-spacing:-.2px}
.poster--growth .pill,.poster--growth .num{color:var(--navy)}
.poster--wellness .pill,.poster--wellness .num{color:var(--orange)}
.poster--innovation .pill,.poster--innovation .num{color:var(--blue)}
.poster--team .pill,.poster--team .num{color:var(--purple)}
</style>
</head>
<body>

<section class="poster poster--growth">
  <h1 class="headline abs" style="left:20px;top:22px;font-size:29.5px">Better Today<br>Than Yesterday</h1>
  <p class="tagline abs" style="left:21px;top:80px;font-size:14.5px;color:var(--orange-brand)">Personal and Professional Growth</p>
  <div class="abs" style="left:17px;top:124px">
    <span class="pill">Leadership Development Programs</span>
    <ul class="list">
      <li><span class="num">1</span>Supervisor Training</li>
      <li><span class="num">2</span>Women’s Leadership</li>
      <li><span class="num">3</span>Leadership Meet-Ups</li>
      <li><span class="num">4</span>MBA Program</li>
    </ul>
  </div>
  <div class="abs" style="left:17px;top:190px">
    <span class="pill">Staff Development</span>
    <ul class="list">
      <li><span class="num">1</span>Continuing Education Fund</li>
      <li><span class="num">2</span>Book Club</li>
      <li><span class="num">3</span>Pelmaroq University</li>
      <li><span class="num">4</span>Mentorship</li>
      <li><span class="num">5</span>Learning Libraries</li>
      <li><span class="num">6</span>Department Wide Training Events</li>
    </ul>
  </div>
  <div class="diamond" role="img" aria-label="Growth campaign icon" style="left:154px;top:149px;width:80px;height:80px;background:var(--orange-brand)"></div>
  <p class="copy abs" style="left:22px;top:287px;width:222px;text-align:center">We are committed to helping you build on your strengths and passions and support you your career advancement goals. We have a variety of training and development programs available to help you reach your top potential!</p>
  <svg class="base" viewBox="0 0 265 37" preserveAspectRatio="none"><path d="M0 14 Q132.5 -12 265 14 V37 H0Z" fill="#fff"/></svg>
  <div class="brand"><span class="brand__mark"></span><span class="brand__name">Pelmaroq</span></div>
</section>

<section class="poster poster--wellness">
  <h1 class="headline abs" style="left:18px;top:20px;font-size:29.5px;color:var(--yellow)">Perform at<br>Highest<br>Capacity</h1>
  <p class="tagline abs" style="left:19px;top:103px;font-size:14px">Be Your Best Self</p>
  <div class="diamond" role="img" aria-label="Wellness campaign icon" style="left:165px;top:57px;width:74px;height:74px;background:var(--amber)"></div>
  <p class="copy abs" style="left:19px;top:137px;width:170px">We are committed to providing programs that bring focus to your health and overall personal wellness to encourage a well balanced life</p>
  <div class="abs" style="left:19px;top:186px">
    <span class="pill">i.&nbsp; Healthy Living</span>
    <ul class="list">
      <li><span class="num">1</span>Health and wellness seminars</li>
      <li><span class="num">2</span>Nutrition: Fruit Delivery</li>
    </ul>
  </div>
  <div class="abs" style="left:19px;top:225px">
    <span class="pill">iii. Creativity</span>
    <ul class="list">
      <li><span class="num">1</span>Painting</li>
      <li><span class="num">2</span>Photography Club</li>
      <li><span class="num">3</span>Virtual Trivia</li>
    </ul>
  </div>
  <div class="abs" style="left:19px;top:273px">
    <span class="pill">v. Financial</span>
    <ul class="list">
      <li><span class="num">1</span>401(k)</li>
      <li><span class="num">2</span>Retirement education/financial planning seminars</li>
      <li><span class="num">3</span>Global Insurance Program education</li>
    </ul>
  </div>
  <div class="abs" style="left:144px;top:186px">
    <span class="pill">ii. Fitness</span>
    <ul class="list">
      <li><span class="num">1</span>Step Challenge</li>
      <li><span class="num">2</span>Virtual 5k</li>
      <li><span class="num">3</span>Recess</li>
      <li><span class="num">4</span>Golf Lessons</li>
      <li><span class="num">5</span>Ping Pong Club</li>
    </ul>
  </div>
  <div class="abs" style="left:144px;top:253px">
    <span class="pill">iv. Mental Health</span>
    <ul class="list">
      <li><span class="num">1</span>Massage Therapy</li>
      <li><span class="num">2</span>EAP Education</li>
    </ul>
  </div>
  <svg class="base" viewBox="0 0 265 37" preserveAspectRatio="none"><path d="M0 14 Q132.5 -12 265 14 V37 H0Z" fill="#fff"/></svg>
  <div class="brand"><span class="brand__mark"></span><span class="brand__name">Pelmaroq</span></div>
</section>

<section class="poster poster--innovation">
  <h1 class="headline abs" style="left:23px;top:21px;font-size:28.5px">Passionate<br>Urgent and<br>Driven to<br>Success</h1>
  <p class="tagline abs" style="left:23px;top:137px;font-size:14px">Innovation and Strategy</p>
  <p class="copy abs" style="left:23px;top:172px;width:225px">We are committed to helping you connect the dots both in the industry and with our internal goals , mission, and vision.</p>
  <div class="diamond" role="img" aria-label="Innovation campaign icon" style="left:34px;top:227px;width:71px;height:71px;background:var(--green)"></div>
  <div class="abs" style="left:129px;top:227px"><span class="pill">i. Quarterly All-Hands</span></div>
  <div class="abs" style="left:129px;top:250px">
    <span class="pill">ii. Lumiverse</span>
    <ul class="list">
      <li style="align-items:flex-start;line-height:9px"><span class="num" style="margin-top:1px">1</span>Internally: Departmental<br>and Product Updates</li>
      <li><span class="num">2</span>Externally: Industry Knowledge</li>
      <li><span class="num">3</span>Culturally: Peer to Peer Community</li>
    </ul>
  </div>
  <svg class="base" viewBox="0 0 265 37" preserveAspectRatio="none"><path d="M0 14 Q132.5 -12 265 14 V37 H0Z" fill="#fff"/></svg>
  <div class="brand"><span class="brand__mark"></span><span class="brand__name">Pelmaroq</span></div>
</section>

<section class="poster poster--team">
  <h1 class="headline abs" style="left:0;width:265px;text-align:center;top:8px;font-size:45px;color:var(--yellow);line-height:.98">Succeed<br>as a Team</h1>
  <p class="tagline abs" style="left:0;width:265px;text-align:center;top:104px;font-size:14.5px">Cultivating Collaboration</p>
  <p class="abs" style="left:22px;top:132px;font-size:7.5px;font-weight:700;color:var(--yellow)">TEAM BUILDING EVENTS</p>
  <div class="abs" style="left:22px;top:145px">
    <span class="pill">1. Employee Focused</span>
    <ul class="list">
      <li><span class="num">a</span>Summer Picnic</li>
      <li><span class="num">b</span>Employee Appreciation</li>
      <li><span class="num">c</span>Diwali</li>
      <li><span class="num">d</span>Holiday Party</li>
      <li><span class="num">e</span>Department Appreciation</li>
    </ul>
  </div>
  <div class="abs" style="left:22px;top:216px">
    <span class="pill">2. Family Friendly</span>
    <ul class="list">
      <li><span class="num">a</span>Halloween</li>
      <li><span class="num">b</span>Bring your Kids to Work Day</li>
    </ul>
  </div>
  <div class="abs" style="left:22px;top:259px">
    <span class="pill">3. Awards</span>
    <ul class="list">
      <li><span class="num">a</span>Peer to Peer: QuickNod Awards</li>
      <li><span class="num">b</span>Leadership: Crest of Merit</li>
    </ul>
  </div>
  <div class="abs" style="left:22px;top:302px">
    <span class="pill">4. Surveys</span>
    <ul class="list">
      <li><span class="num">a</span>New Hire</li>
      <li><span class="num">b</span>Employee Engagement</li>
    </ul>
  </div>
  <p class="copy abs" style="left:131px;top:132px;width:118px">We are committed to creating a culture of appreciation, teamwork, and supporting an open communication. All feedback and ideas are welcome</p>
  <div class="diamond" role="img" aria-label="Teamwork campaign icon" style="left:162px;top:223px;width:71px;height:71px;background:var(--yellow)"></div>
  <svg class="base" viewBox="0 0 265 37" preserveAspectRatio="none"><path d="M0 14 Q132.5 -12 265 14 V37 H0Z" fill="#fff"/></svg>
  <div class="brand"><span class="brand__mark"></span><span class="brand__name">Pelmaroq</span></div>
</section>

</body>
</html>
```